Spa needs a storefront sticker design

For our city spa we need window stickers for the shop window.
The window stickers must fill the entire windows.
What we have in mind is that our logo is visible in the middle with graphic shapes surrounding it to stand out extra on the main street. The design is going to be printed in white and cut out. To give an impression of what we have in mind, our logo is attached with various example designs.
please supply your final file in the following extensions: – Eps file (*.eps) – Photoshop file (*.psd) – Adobe Portable Document (*.pdf) – Jpeg file ( *.jpg, *.jpeg) – Tiff file (*.tif, *.tiff)– Text in letter outlines
A photo of the shop window will be added tomorrow, including the exact dimensions so that the design can be adjusted accordingly

```html
<!DOCTYPE html>
<html lang="en">
<head>
<meta charset="utf-8">
<title>Sereno Baby &amp; Spa – Window Sticker</title>
<link rel="stylesheet" href="https://fonts.googleapis.com/css2?family=Alegreya:wght@500;700&display=swap">
<style>
  :root {
    --window-black: #000000;
    --vinyl-white: #ffffff;
  }
  * { margin: 0; padding: 0; box-sizing: border-box; }
  html, body {
    width: 1200px;
    height: 1000px;
    overflow: hidden;
    background: var(--window-black);
  }
  .sticker-canvas {
    position: relative;
    width: 1200px;
    height: 1000px;
    background: var(--window-black);
  }
  .cut-line {
    position: absolute;
    left: 93px;
    top: 147px;
    width: 1013px;
    height: 706px;
    border: 1px solid var(--vinyl-white);
  }
  .ornament {
    position: absolute;
    display: block;
  }
  .ornament path { fill: var(--vinyl-white); }
  .ornament--top-left {
    left: 94px;
    top: 150px;
    width: 478px;
    height: 364px;
  }
  .ornament--bottom-right {
    left: 643px;
    top: 474px;
    width: 462px;
    height: 378px;
  }
  .brand {
    position: absolute;
    left: 400px;
    top: 450px;
    width: 400px;
    color: var(--vinyl-white);
    font-family: "Alegreya", Georgia, serif;
  }
  .brand__dot {
    display: block;
    width: 12px;
    height: 12px;
    margin: 0 auto;
    border-radius: 50%;
    background: var(--vinyl-white);
  }
  .brand__name {
    margin-top: 14px;
    text-align: center;
    font-weight: 500;
    font-size: 50px;
    letter-spacing: 8px;
    line-height: 1;
    padding-left: 8px;
  }
  .brand__tagline {
    position: absolute;
    left: 154px;
    top: 92px;
    width: 100px;
    text-align: center;
    font-weight: 700;
    font-size: 17px;
    line-height: 1;
  }
</style>
</head>
<body>
  <main class="sticker-canvas">
    <div class="cut-line"></div>

    <svg class="ornament ornament--top-left" viewBox="0 0 478 364" role="img"
         aria-label="White flowing flourish ornament with spirals, leaf strokes and dotted trails sweeping from the left edge">
      <path d="M0,300 C110,270 170,140 290,120 C390,104 440,50 478,0 C466,90 410,160 310,170 C210,180 160,300 0,345 Z"/>
    </svg>
    <svg class="ornament ornament--bottom-right" viewBox="0 0 462 378" role="img"
         aria-label="White flowing flourish ornament with spirals, leaf strokes and dotted trails sweeping to the right edge">
      <path d="M462,70 C352,100 292,230 172,250 C72,266 22,320 0,378 C10,290 66,214 162,204 C262,194 302,78 462,30 Z"/>
    </svg>

    <div class="brand">
      <span class="brand__dot"></span>
      <div class="brand__name">SERENO</div>
      <div class="brand__tagline">Baby &amp; Spa</div>
    </div>
  </main>
</body>
</html>
```